Flat Belly Design Graphics for Social

I want to create 9 social media graphics (new Instagram size 4:5 (1080 x 1350 pixels) focusing on our Flat Belly Graphics, using the pics attached. Use the attached pics, NO RANDOM STOCK PHOTOGRAPHY. For the color scheme of the graphics, the color palette is attached. YOU MUST POST ALL 9 GRAPHICS IN ONE ENTRY.
Using the 3 titles below, create one set of graphics. 1) with all text, then for the others, use the pictures as detailed below in IMPORTANT:
1. 21-Night Lean Middle Reboot Beyond 50
2. The 20-Second Trim-Core Menu Guide
3. Starlet Tricks to a Slender Midline Beyond 50 - Zero Scalpel Needed
IMPORTANT:
Only use RK Pic 1 and RK Pic 2 with the title, 21-Night Lean Middle Reboot Beyond 50
Only use meal plan1 and meal plan2 pics with the title, 20-Second Trim-Core Menu Guide
Only use starlet tricks 1 and starlet tricks 2 pics with the title, Starlet Tricks to a Slender Midline Beyond 50 - Zero Scalpel Needed
women over 40

```html
<!DOCTYPE html>
<html lang="en">
<head>
<meta charset="utf-8">
<title>Lean Middle Social Set</title>
<link rel="stylesheet" href="https://fonts.googleapis.com/css2?family=Bebas+Neue&family=Lato:wght@400;700;900&display=swap">
<style>
  :root {
    --pink: #e296ab;
    --forest: #334e4c;
    --blush: #fbecee;
    --rose-mist: #f6d9de;
    --paper: #ffffff;
    --display: "Bebas Neue", "Oswald", sans-serif;
    --body: "Lato", "Helvetica Neue", sans-serif;
  }
  * { margin: 0; padding: 0; box-sizing: border-box; }
  html, body { width: 1200px; height: 904px; overflow: hidden; background: var(--paper); }
  .canvas { position: relative; width: 1200px; height: 904px; }

  .panel { position: absolute; overflow: hidden; background: var(--pink); }
  .panel--dark { background: var(--forest); }
  .panel--hero { left: 35px; top: 30px; width: 442px; height: 557px; }
  .col-1 { left: 490px; } .col-2 { left: 723px; } .col-3 { left: 954px; }
  .row-1 { top: 28px; } .row-2 { top: 314px; } .row-3 { top: 599px; }
  .tile { width: 218px; height: 273px; }

  .abs { position: absolute; }
  .display { font-family: var(--display); font-weight: 400; line-height: 0.86; white-space: nowrap; }
  .label { font-family: var(--body); font-weight: 700; line-height: 1.05; white-space: nowrap; }
  .center-x { left: 0; right: 0; text-align: center; }
  .c-blush { color: var(--blush); } .c-mist { color: var(--rose-mist); }
  .c-forest { color: var(--forest); } .c-pink { color: var(--pink); }

  /* hero */
  .hero-curve { position: absolute; inset: 0; }
  .hero-number { left: 24px; top: 78px; font-size: 300px; letter-spacing: -6px; }
  .hero-unit { left: 262px; top: 200px; font-size: 78px; }
  .hero-title { left: 46px; top: 318px; font-size: 92px; line-height: 0.8; }
  .hero-tag { left: 52px; top: 502px; font-size: 23px; }

  /* starlet tiles */
  .kicker { font-size: 17px; letter-spacing: 0.2px; }
  .rule { height: 1px; background: var(--forest); }
  .ribbon { font-family: var(--body); font-weight: 700; font-size: 12.5px; padding: 3px 6px; white-space: nowrap; }

  .s1-kicker { top: 26px; }
  .s1-rule { left: 82px; width: 56px; top: 62px; }
  .s1-title { top: 76px; font-size: 55px; line-height: 0.92; }
  .s1-sub { top: 192px; font-size: 37px; }
  .s1-ribbon { left: 23px; top: 231px; width: 172px; text-align: center; background: var(--blush); color: var(--forest); }

  .s2-block { left: 12px; top: 38px; width: 200px; transform: rotate(-8deg); transform-origin: center; text-align: center; }
  .s2-kicker { font-size: 17px; color: var(--blush); }
  .s2-title { font-size: 60px; line-height: 0.88; color: var(--forest); text-shadow: 3px -2px 0 var(--blush); }
  .s2-sub { font-size: 38px; color: var(--forest); text-shadow: 2px -2px 0 var(--blush); }
  .s2-ribbon { display: inline-block; margin-top: 4px; background: var(--blush); color: var(--forest); }

  .s3-kicker { top: 15px; }
  .s3-disc { left: 16px; top: 63px; width: 188px; height: 188px; border-radius: 50%; background: var(--rose-mist); }
  .s3-title { top: 80px; font-size: 52px; line-height: 0.92; }
  .s3-sub { top: 186px; font-size: 37px; }
  .s3-ribbon { left: 23px; top: 231px; width: 172px; text-align: center; background: var(--forest); color: var(--blush); }

  /* night tiles */
  .n1-band { left: 70px; top: 0; width: 79px; height: 99px; background: var(--pink); }
  .n1-number { left: 70px; width: 79px; top: 16px; text-align: center; font-size: 92px; }
  .n1-unit { top: 104px; font-size: 76px; }
  .n1-title { top: 183px; font-size: 38px; }
  .n1-rule { left: 28px; width: 162px; top: 224px; background: var(--pink); opacity: 0.6; }
  .n1-tag { top: 236px; font-size: 18px; }

  .n2-number { left: 30px; top: 10px; font-size: 150px; letter-spacing: -3px; }
  .n2-band { left: 112px; top: 93px; width: 106px; height: 38px; background: var(--rose-mist); }
  .n2-unit { left: 116px; top: 94px; font-size: 38px; }
  .n2-title { top: 142px; font-size: 50px; line-height: 0.84; }
  .n2-tag { top: 238px; font-size: 18px; }

  .n3-figure { position: absolute; inset: 0; }
  .n3-number { top: 18px; font-size: 124px; }
  .n3-title { top: 126px; font-size: 38px; line-height: 0.86; }
  .n3-tag { top: 214px; font-size: 18px; }

  /* seconds tiles */
  .m1-outline { right: 30px; top: 0px; width: 140px; height: 150px; }
  .m1-the { left: 32px; top: 128px; font-size: 26px; }
  .m1-unit { left: 34px; top: 154px; font-size: 54px; }
  .m1-title { left: 36px; top: 205px; font-size: 22px; }

  .m2-band { left: 76px; top: 0; width: 110px; height: 150px; background: var(--pink); }
  .m2-number { left: 76px; width: 110px; top: 28px; text-align: center; font-size: 142px; letter-spacing: -4px; }
  .m2-the { left: 34px; top: 128px; font-size: 28px; }
  .m2-unit { left: 34px; top: 155px; font-size: 54px; }
  .m2-title { left: 36px; top: 205px; font-size: 23px; }

  .m3-frame { left: 20px; top: 30px; width: 180px; height: 225px; border: 1px solid var(--forest); }
  .m3-the { left: 88px; top: 18px; padding: 0 6px; background: var(--pink); font-size: 25px; }
  .m3-number { left: 28px; top: 40px; font-size: 170px; letter-spacing: -6px; }
  .m3-unit { left: 150px; top: 40px; width: 150px; font-size: 54px; transform-origin: 0 0; transform: rotate(90deg) translate(0, -50px); text-align: center; line-height: 1; }
  .m3-title { left: 28px; top: 199px; width: 170px; padding: 0 2px; background: var(--pink); text-align: center; font-size: 22px; }
</style>
</head>
<body>
<main class="canvas">

  <!-- Hero -->
  <section class="panel panel--hero" aria-label="21-Night Lean Middle Reboot Beyond 50">
    <svg class="hero-curve" viewBox="0 0 442 557" width="442" height="557" aria-hidden="true">
      <path d="M276 0 C228 60 214 200 248 320 C282 430 322 490 334 557 L442 557 L442 0 Z" fill="var(--forest)"/>
    </svg>
    <div class="abs display hero-number c-blush">21</div>
    <div class="abs display hero-unit c-pink">NIGHTS</div>
    <div class="abs display hero-title c-blush">LEAN<br>MIDDLE</div>
    <div class="abs label hero-tag c-forest">REBOOT BEYOND 50</div>
  </section>

  <!-- Row 1 -->
  <section class="panel tile col-1 row-1" aria-label="Starlet Tricks to a Slender Midline Beyond 50">
    <div class="abs label center-x kicker s1-kicker c-forest">STARLET TRICKS<br>TO A</div>
    <div class="abs rule s1-rule"></div>
    <div class="abs display center-x s1-title c-mist">SLENDER<br>MIDLINE</div>
    <div class="abs display center-x s1-sub c-mist">BEYOND 50</div>
    <div class="abs ribbon s1-ribbon">ZERO SCALPEL NEEDED</div>
  </section>

  <section class="panel panel--dark tile col-2 row-1" aria-label="21-Night Lean Middle Reboot Beyond 50">
    <div class="abs n1-band"></div>
    <div class="abs display n1-number c-forest">21</div>
    <div class="abs display center-x n1-unit c-pink">NIGHTS</div>
    <div class="abs display center-x n1-title c-blush">LEAN MIDDLE</div>
    <div class="abs rule n1-rule"></div>
    <div class="abs label center-x n1-tag c-blush">REBOOT BEYOND 50</div>
  </section>

  <section class="panel tile col-3 row-1" aria-label="The 20-Second Trim-Core Menu Guide">
    <svg class="abs m1-outline" viewBox="0 0 140 150" width="140" height="150" aria-hidden="true">
      <text x="70" y="144" text-anchor="middle" font-family="Bebas Neue, sans-serif" font-size="190" fill="none" stroke="var(--forest)" stroke-width="1.2" letter-spacing="-4">20</text>
    </svg>
    <div class="abs display m1-the c-forest">THE</div>
    <div class="abs display m1-unit c-forest">SECOND</div>
    <div class="abs label m1-title c-blush">TRIM-CORE<br>MENU GUIDE</div>
  </section>

  <!-- Row 2 -->
  <section class="panel panel--dark tile col-1 row-2" aria-label="The 20-Second Trim-Core Menu Guide">
    <div class="abs m2-band"></div>
    <div class="abs display m2-number c-forest">20</div>
    <div class="abs display m2-the c-blush">THE</div>
    <div class="abs display m2-unit c-blush">SECOND</div>
    <div class="abs label m2-title c-blush">TRIM-CORE<br>MENU GUIDE</div>
  </section>

  <section class="panel tile col-2 row-2" aria-label="Starlet Tricks to a Slender Midline Beyond 50">
    <div class="abs s2-block">
      <div class="label s2-kicker">STARLET TRICKS<br>TO A</div>
      <div class="display s2-title">SLENDER<br>MIDLINE</div>
      <div class="display s2-sub">BEYOND 50</div>
      <div class="ribbon s2-ribbon">ZERO SCALPEL NEEDED</div>
    </div>
  </section>

  <section class="panel tile col-3 row-2" aria-label="21-Night Lean Middle Reboot Beyond 50">
    <div class="abs display n2-number c-mist">21</div>
    <div class="abs n2-band"></div>
    <div class="abs display n2-unit c-pink">NIGHTS</div>
    <div class="abs display center-x n2-title c-forest">LEAN<br>MIDDLE</div>
    <div class="abs label center-x n2-tag c-mist">REBOOT BEYOND 50</div>
  </section>

  <!-- Row 3 -->
  <section class="panel tile col-1 row-3" aria-label="Starlet Tricks to a Slender Midline Beyond 50">
    <div class="abs label center-x kicker s3-kicker c-forest">STARLET TRICKS<br>TO A</div>
    <div class="abs s3-disc"></div>
    <div class="abs display center-x s3-title c-pink">SLENDER<br>MIDLINE</div>
    <div class="abs display center-x s3-sub c-pink">BEYOND 50</div>
    <div class="abs ribbon s3-ribbon">ZERO SCALPEL NEEDED</div>
  </section>

  <section class="panel tile col-2 row-3" aria-label="21-Night Lean Middle Reboot Beyond 50">
    <svg class="n3-figure" viewBox="0 0 218 273" width="218" height="273" role="img" aria-label="Slim waist silhouette in swimwear">
      <defs>
        <linearGradient id="figureTone" x1="0" y1="0" x2="1" y2="0">
          <stop offset="0" stop-color="#334e4c"/>
          <stop offset="0.22" stop-color="#e296ab"/>
          <stop offset="0.78" stop-color="#e296ab"/>
          <stop offset="1" stop-color="#334e4c"/>
        </linearGradient>
      </defs>
      <rect width="218" height="273" fill="url(#figureTone)"/>
    </svg>
    <div class="abs display center-x n3-number c-mist">21</div>
    <div class="abs display center-x n3-title c-blush">NIGHTS LEAN<br>MIDDLE</div>
    <div class="abs label center-x n3-tag c-blush">REBOOT BEYOND 50</div>
  </section>

  <section class="panel tile col-3 row-3" aria-label="The 20-Second Trim-Core Menu Guide">
    <div class="abs m3-frame"></div>
    <div class="abs display m3-the c-forest">THE</div>
    <div class="abs display m3-number c-mist">20</div>
    <div class="abs display m3-unit c-mist">SECOND</div>
    <div class="abs label m3-title c-forest">TRIM-CORE<br>MENU GUIDE</div>
  </section>

</main>
</body>
</html>
```